Professional Engineering Web Design

Project Brief: Website Redesign for Mechanical Design Consultancy
Project Overview
I want to update and improve my current website to create a more professional, modern, and high-credibility online presence for my mechanical design consultancy.

Current site: https://valtrix.design/

The new website must communicate expertise, precision, and trust—matching the standard of top engineering and product design agencies.

Reference Websites (Style + Structure Inspiration)
These represent the quality, cleanliness, and professionalism I want to achieve:

https://plovenproductdesign.com/
https://www.quorvel.com/
https://dambrise-uk.com/
Brand Look
Professional, modern, engineering-focused aesthetic
Clean layouts and strong typography
High-quality imagery conveying precision, innovation, and mechanical expertise
Colour scheme and styling must follow my existing logo (attached in project)
Platform Requirements
The website must be built on WordPress
Should use a clean, flexible theme or modern page builder (Elementor, Gutenberg, Bricks, or similar)
Avoid overly complex custom coding so I can easily edit content later
Final deliverable must allow me to manage and update content without developer assistance
Functionality
Fast-loading, lightweight, and smooth user experience
Clean animations and transitions similar to the reference sites
Fully mobile responsive
Clear navigation and strong visual hierarchy
Contact forms optimised for lead generation
Optional: subtle scroll effects, case study sliders, icon animations, etc.
SEO Aspirations
Developer should recommend and implement a modern SEO strategy
Proper on-page SEO setup (titles, meta, schema, alt tags, heading structure)
Optimised site architecture for ranking and crawling
Aim: Generate leads through improved visibility and keyword targeting
Optional but useful: Google Analytics, Google Search Console setup
User Journeys
(Recommended structure)

The site should be crafted around clear, intuitive journeys for each type of visitor:

Potential new clients
Quickly understand what services I offer
View examples of past work / case studies
See credibility indicators (process, expertise, industries served)
Easily contact me or request a project discussion
Returning clients
Access updated portfolio items
Find contact details or book follow-up work easily
General visitors discovering through SEO
Be guided to core service areas
Understand my value proposition quickly
Be invited to learn more or make contact
The developer should design the structure to support these journeys smoothly.

Maintenance Expectations
Website will be maintained by me, so it should be easy to update using relatively basic WordPress skills
Use modular templates and simple backend structure
Avoid unnecessary plugins
Provide brief handover documentation if required
Hosting Preferences
Site is currently hosted via a family member
Open to discussing moving to a paid, reliable hosting provider if preferable for performance and maintainability
Developer may advise on the best hosting setup for WordPress
Content
Most content can be taken from the existing website
Developer is welcome to suggest improvements to structure, layout, and imagery
Must remain easy for me to edit or add new content later (e.g., new projects)
Deliverables
Fully built WordPress website
Clean, professional, modern design inspired by the reference sites
Mobile-responsive across all devices
SEO-ready structure and optimisations
Transfer of website and admin rights
Any design assets, templates, or documentation used

Coding

```html
<!DOCTYPE html>
<html lang="en">
<head>
<meta charset="utf-8">
<title>Valtrix Mechanical Design</title>
<link href="https://fonts.googleapis.com/css2?family=Rajdhani:wght@600;700&family=Red+Hat+Text:wght@400;500;700&display=swap" rel="stylesheet">
<style>
:root{
  --blue:#1c43f0;
  --ink:#1d1d1f;
  --dark:#1e1e1e;
  --text:#444;
  --muted:#6b6b6b;
  --line:#d8d8d8;
  --light:#f1f1f1;
  --white:#fff;
}
*{box-sizing:border-box;margin:0;padding:0}
html,body{width:1200px;height:5249px;overflow:hidden}
body{position:relative;font-family:"Red Hat Text",Arial,sans-serif;color:var(--text);background:var(--white)}
.abs{position:absolute}
.heading{font-family:"Rajdhani",Arial,sans-serif;font-weight:700;color:var(--ink);text-transform:uppercase;letter-spacing:.5px}
.btn{position:absolute;display:flex;align-items:center;justify-content:center;background:var(--blue);color:var(--white);font-size:12px;font-weight:700;text-transform:uppercase}
.eyebrow{font-size:11px;text-transform:uppercase;color:var(--ink);text-align:center;width:100%}
.arrows{position:absolute;display:flex;gap:12px}
.arrows span{width:42px;height:42px;border:1.5px solid #333;border-radius:50%;display:flex;align-items:center;justify-content:center}
.arrows.light span{border-color:#bbb}
/* header */
.site-header{top:0;left:0;width:1200px;height:90px;background:var(--white)}
.brand{display:flex;align-items:center;gap:10px}
.brand-mark{width:58px;height:58px;border-radius:50%;background:var(--blue)}
.brand-name{font-family:"Rajdhani",sans-serif;font-weight:700;color:var(--blue);line-height:1}
.site-nav{left:480px;top:0;height:90px;display:flex;align-items:center}
.site-nav a{font-size:13px;color:#333;text-decoration:none;padding:0 24px;border-left:1px solid #ddd;text-transform:uppercase}
.site-nav a:first-child{border-left:none;color:var(--blue);font-weight:700}
.nav-cta{left:959px;top:24px;width:151px;height:43px;border:2px solid #333;font-size:12px;font-weight:700;display:flex;align-items:center;justify-content:center;color:var(--ink)}
/* hero */
.hero{top:90px;left:0;width:1200px;height:645px;background:var(--dark)}
.hero-title{left:90px;top:145px;font-size:80px;line-height:70px;color:var(--white)}
.hero-sub{left:90px;top:305px;font-size:22px;color:#ddd;letter-spacing:-.5px}
.hero-btn{left:90px;top:354px;width:169px;height:49px;background:var(--white);color:var(--ink);font-size:12px;font-weight:700;display:flex;align-items:center;justify-content:center}
.scroll-hint{left:92px;top:570px;width:18px;height:30px;border:2px solid #ccc;border-radius:9px}
.hero-photo{left:407px;top:122px;width:764px;height:676px;clip-path:polygon(357px 0,764px 0,469px 100%,0 100%);background:linear-gradient(120deg,#2d3b6c,#8d96b3 40%,#d8d8de 60%,#1d3fd8);box-shadow:0 30px 40px rgba(0,0,0,.2)}
/* about */
.about-bar-top{left:326px;top:915px;width:261px;height:46px;background:var(--blue);clip-path:polygon(22px 0,100% 0,calc(100% - 22px) 100%,0 100%)}
.about-bar-bottom{left:146px;top:1344px;width:252px;height:47px;background:var(--blue);clip-path:polygon(22px 0,100% 0,calc(100% - 22px) 100%,0 100%)}
.about-photo{left:104px;top:961px;width:509px;height:383px;background:linear-gradient(135deg,#8a9a6c,#5e6d4e 50%,#2c3a56);box-shadow:0 20px 30px rgba(0,0,0,.15)}
.about-title{left:658px;top:1030px;font-size:38px}
.about-text{left:658px;top:1085px;width:440px;font-size:12.5px;line-height:22px;color:var(--muted)}
.about-btn{left:658px;top:1218px;width:247px;height:49px}
/* services */
.services-eyebrow{top:1502px;left:0}
.services-title{top:1524px;left:0;width:1200px;text-align:center;font-size:38px;line-height:44px}
.card{position:absolute;top:1646px;width:322px;height:462px;border:1px solid var(--line);background:var(--white)}
.card-img{height:244px;width:100%}
.card h3{font-family:"Red Hat Text",sans-serif;font-size:15px;font-weight:700;color:var(--ink);margin:26px 0 0 27px;text-transform:uppercase}
.card p{font-size:12px;line-height:20px;color:var(--muted);margin:10px 27px 0}
.card .btn{left:27px;bottom:32px;width:124px;height:48px}
/* expertise */
.expertise{top:2300px;left:0;width:1200px;height:540px;background:linear-gradient(90deg,#1e1e1e 50%,#2a2522 85%,#3b2b24)}
.exp-title{left:90px;top:90px;font-size:38px;color:var(--white)}
.exp-item{left:90px;width:480px;height:110px;display:flex;gap:14px;align-items:flex-start}
.exp-item+.exp-item{border-top:1px solid #555}
.exp-icon{flex:none;width:74px;height:74px;border-radius:50%;background:var(--blue);display:flex;align-items:center;justify-content:center}
.exp-item h4{font-family:"Rajdhani",sans-serif;font-size:18px;color:var(--white);margin-top:4px;text-transform:uppercase}
.exp-item p{font-size:12.5px;line-height:19px;color:#ddd;margin-top:4px;width:370px}
.exp-slash{left:688px;top:49px;width:402px;height:438px;background:var(--blue);clip-path:polygon(145px 0,100% 0,257px 100%,0 100%)}
.exp-product{left:665px;top:90px;width:450px;height:330px;border-radius:40% 30% 35% 30%;background:radial-gradient(ellipse at 55% 45%,#e6e6e6,#9c9c9c 55%,rgba(60,60,60,.9) 75%,transparent 76%)}
/* work */
.work-title{top:2930px;left:0;width:1200px;text-align:center;font-size:38px}
.work-sub{top:2988px;left:0;width:1200px;text-align:center;font-size:13px;color:var(--muted)}
.work-grid{top:3041px;left:90px;width:1020px;height:477px}
.work-cell{position:absolute;width:340px;height:239px;border:1px solid var(--line);overflow:hidden}
.work-shadow{position:absolute;left:78px;top:105px;width:200px;height:134px;background:#e6e6e6;clip-path:polygon(60% 0,100% 0,40% 100%,0 100%)}
.work-item{position:absolute;left:95px;top:45px;width:150px;height:120px;border-radius:18px}
.work-all{left:760px;top:354px;display:flex;align-items:center;gap:14px;font-size:12px;color:var(--ink);text-transform:uppercase}
.work-all i{width:32px;height:32px;background:var(--blue);display:flex;align-items:center;justify-content:center}
/* contact */
.contact{top:3628px;left:0;width:1200px;height:1216px;background:var(--light)}
.contact-eyebrow{top:65px;left:0}
.contact-title{top:80px;left:0;width:1200px;text-align:center;font-size:38px}
.form{left:181px;top:159px;width:835px;height:470px;background:var(--white)}
.field{position:absolute}
.field label{display:block;font-size:11px;font-weight:700;color:var(--ink);text-transform:uppercase;margin-bottom:6px}
.field label b{color:#e23}
.field div{border:1px solid #ccc;height:45px;font-size:12px;color:#999;padding:13px 18px}
.submit{left:308px;top:373px;width:218px;height:51px;gap:8px}
.reviews-eyebrow{top:734px;left:0}
.reviews-title{top:752px;left:0;width:1200px;text-align:center;font-size:38px}
.quote-mark{left:88px;top:873px;font-family:Georgia,serif;font-size:160px;line-height:160px;color:#c9c9c9}
.quote{left:190px;top:830px;width:820px;text-align:center;font-size:17px;line-height:31px;color:#333}
.client{top:982px;left:0;width:1200px;text-align:center;font-size:12px;font-weight:700;color:var(--ink)}
.client-role{top:1008px;left:0;width:1200px;text-align:center;font-size:12px;color:#333}
/* footer */
.site-footer{top:4844px;left:0;width:1200px;height:405px;background:var(--dark)}
.footer-brand{left:452px;top:64px}
.footer-nav{top:197px;left:0;width:1200px;display:flex;justify-content:center;gap:50px}
.footer-nav a{font-size:13px;color:var(--white);text-decoration:none;text-transform:uppercase}
.social{top:245px;left:0;width:1200px;display:flex;justify-content:center;gap:12px}
.social span{width:42px;height:42px;border-radius:50%;background:#333}
.copyright{top:366px;left:0;width:1200px;text-align:center;font-size:13px;color:var(--white)}
.to-top{left:1130px;top:4970px;width:48px;height:48px;border-radius:50%;background:var(--blue);display:flex;align-items:center;justify-content:center}
</style>
</head>
<body>

<header class="abs site-header">
  <div class="abs brand" style="left:90px;top:15px">
    <span class="brand-mark"></span>
    <span class="brand-name"><span style="font-size:34px">valtrix</span><br><span style="font-size:11px;font-family:'Red Hat Text',sans-serif">MECHANICAL DESIGN</span></span>
  </div>
  <nav class="abs site-nav">
    <a href="#">Home</a><a href="#">About Us</a><a href="#">Our Services</a><a href="#">Portfolio</a>
  </nav>
  <a class="abs nav-cta">CONTACT US</a>
</header>

<section class="abs hero">
  <h1 class="abs heading hero-title">Mechanical<br>CAD Design</h1>
  <p class="abs hero-sub">CUTTING EDGE ENGINEERING</p>
  <a class="abs hero-btn">FIND OUT MORE</a>
  <span class="abs scroll-hint"></span>
  <div class="arrows light" style="left:1027px;top:563px">
    <span><svg width="14" height="10" viewBox="0 0 14 10"><path d="M13 5H1M5 1L1 5l4 4" stroke="#fff" fill="none" stroke-width="1.4"/></svg></span>
    <span><svg width="14" height="10" viewBox="0 0 14 10"><path d="M1 5h12M9 1l4 4-4 4" stroke="#fff" fill="none" stroke-width="1.4"/></svg></span>
  </div>
</section>
<div class="abs hero-photo" role="img" aria-label="Engineer working at a CAD workstation with 3D models on screen"></div>

<section>
  <div class="abs about-bar-top"></div>
  <div class="abs about-photo" role="img" aria-label="Portrait of the chief engineer"></div>
  <div class="abs about-bar-bottom"></div>
  <h2 class="abs heading about-title">About Us</h2>
  <p class="abs about-text">Aldric Penhale is the Chief Engineer at Valtrix Mechanical Design. He has 11 years experience working as a mechanical design engineer in multiple industries including high performance automotive, consumer products, medical, industrial plus many more. He has worked in multiple roles across a wide range of products.</p>
  <a class="btn about-btn">TELL US ABOUT YOUR IDEAS</a>
</section>

<section>
  <p class="abs eyebrow services-eyebrow">Our Services</p>
  <h2 class="abs heading services-title">We offer a comprehensive<br>design service</h2>
  <article class="card" style="left:98px">
    <div class="card-img" role="img" aria-label="Hand drafting technical gear drawings" style="background:linear-gradient(135deg,#dfe6ee,#b7c3d0)"></div>
    <h3>Mechanical Design</h3>
    <p>Our primary service is mechanical design from initial concepts through to production manufacture. Our proven methodology...</p>
    <a class="btn">SEE MORE</a>
  </article>
  <article class="card" style="left:438px">
    <div class="card-img" role="img" aria-label="Two engineers reviewing a design together" style="background:linear-gradient(135deg,#ececec,#b9b1a8)"></div>
    <h3>Design Consultancy</h3>
    <p>If you've got a great idea and want to begin developing it but don't know where to start, we can help...</p>
    <a class="btn">SEE MORE</a>
  </article>
  <article class="card" style="left:780px">
    <div class="card-img" role="img" aria-label="Team gathered around a table of project plans" style="background:linear-gradient(135deg,#d7d4cf,#8e8a86)"></div>
    <h3>Project Management</h3>
    <p>We have worked on hundreds of projects over the years - from very small to projects that span many years. Each project...</p>
    <a class="btn">SEE MORE</a>
  </article>
  <div class="arrows" style="left:550px;top:2148px">
    <span><svg width="14" height="10" viewBox="0 0 14 10"><path d="M13 5H1M5 1L1 5l4 4" stroke="#333" fill="none" stroke-width="1.4"/></svg></span>
    <span><svg width="14" height="10" viewBox="0 0 14 10"><path d="M1 5h12M9 1l4 4-4 4" stroke="#333" fill="none" stroke-width="1.4"/></svg></span>
  </div>
</section>

<section class="abs expertise">
  <h2 class="abs heading exp-title">Our Expertise</h2>
  <div class="abs exp-item" style="top:155px">
    <span class="exp-icon"><svg width="34" height="30" viewBox="0 0 34 30" fill="none" stroke="#fff" stroke-width="1.6"><rect x="2" y="2" width="30" height="22"/><rect x="9" y="7" width="16" height="12"/><path d="M12 28h10"/></svg></span>
    <div><h4>Bespoke Product Design</h4><p>Innovative design from concept through the full development life cycle.</p></div>
  </div>
  <div class="abs exp-item" style="top:265px;padding-top:10px">
    <span class="exp-icon"><svg width="32" height="32" viewBox="0 0 32 32" fill="none" stroke="#fff" stroke-width="1.6"><path d="M16 2l12 7v14l-12 7-12-7V9z"/><path d="M4 9l12 7 12-7M16 16v14"/></svg></span>
    <div><h4>3D Modelling and Drawings</h4><p>We create 3D CAD, 2D engineering drawings and photorealistic renders</p></div>
  </div>
  <div class="abs exp-item" style="top:375px;padding-top:10px">
    <span class="exp-icon"><svg width="32" height="32" viewBox="0 0 32 32" fill="none" stroke="#fff" stroke-width="1.6"><path d="M6 4h20M16 4v8"/><rect x="6" y="12" width="20" height="12"/><path d="M4 28h24"/><circle cx="16" cy="18" r="3"/></svg></span>
    <div><h4>Design for Manufacture</h4><p>Creating designs optimised for prototype and production manufacture</p></div>
  </div>
  <div class="abs exp-slash"></div>
  <div class="abs exp-product" role="img" aria-label="Rendered automotive gearbox assembly"></div>
</section>

<section>
  <h2 class="abs heading work-title">Our Work</h2>
  <p class="abs work-sub">A small selection of our previous projects</p>
  <div class="abs work-grid">
    <div class="work-cell" style="left:0;top:0"><span class="work-shadow"></span><span class="work-item" role="img" aria-label="Alloy wheel render" style="border-radius:50%;left:105px;width:130px;height:130px;background:radial-gradient(circle,#555 15%,#ddd 40%,#777 70%,#333)"></span></div>
    <div class="work-cell" style="left:340px;top:0"><span class="work-shadow"></span><span class="work-item" role="img" aria-label="Gearbox render" style="background:linear-gradient(135deg,#555,#1d1d1d)"></span></div>
    <div class="work-cell" style="left:680px;top:0"><span class="work-shadow"></span><span class="work-item" role="img" aria-label="Driving rig frame render" style="background:linear-gradient(135deg,#ddd6b8,#333)"></span></div>
    <div class="work-cell" style="left:0;top:238px"><span class="work-shadow"></span><span class="work-item" role="img" aria-label="Linear actuator render" style="height:60px;top:80px;background:linear-gradient(90deg,#222,#d9a521)"></span></div>
    <div class="work-cell" style="left:340px;top:238px"><span class="work-shadow"></span><span class="work-item" role="img" aria-label="Industrial machine render" style="left:120px;width:100px;height:140px;border-radius:4px;background:linear-gradient(135deg,#9aa0a6,#4c5258)"></span></div>
    <a class="abs work-all">View all products <i><svg width="12" height="10" viewBox="0 0 12 10"><path d="M1 1l4 4-4 4M6 1l4 4-4 4" stroke="#fff" fill="none" stroke-width="1.4"/></svg></i></a>
  </div>
</section>

<section class="abs contact">
  <p class="abs eyebrow contact-eyebrow">Contact Us</p>
  <h2 class="abs heading contact-title">Get in touch with us</h2>
  <form class="abs form">
    <div class="field" style="left:94px;top:42px;width:316px"><label>Name<b>*</b></label><div>Enter name</div></div>
    <div class="field" style="left:424px;top:42px;width:314px"><label>Email<b>*</b></label><div>Enter email</div></div>
    <div class="field" style="left:94px;top:127px;width:644px"><label>Company name<b>*</b></label><div>Enter company name</div></div>
    <div class="field" style="left:94px;top:212px;width:644px"><label>Comment or message<b>*</b></label><div style="height:106px">Type your message</div></div>
    <a class="btn submit"><svg width="14" height="14" viewBox="0 0 14 14"><path d="M13 1L1 6l4 2 1 5 2-3 3 2z" fill="#fff"/></svg>SUBMIT ENQUIRY</a>
  </form>
  <p class="abs eyebrow reviews-eyebrow">Client Reviews</p>
  <h2 class="abs heading reviews-title">Case studies and testimonials</h2>
  <span class="abs quote-mark">&ldquo;</span>
  <p class="abs quote">"5* Aldric was amazing. His communication was excellent, responded very quickly, started working on the project the same day I purchased, and problem solved every little detail with my design. He clearly knows what he is talking about and has put in all his efforts to create a perfect design. I highly recommend his service and will use him again on my next project."</p>
  <p class="abs client">RENATA VASQUELL</p>
  <p class="abs client-role">Client</p>
  <div class="arrows" style="left:550px;top:1056px">
    <span><svg width="14" height="10" viewBox="0 0 14 10"><path d="M13 5H1M5 1L1 5l4 4" stroke="#333" fill="none" stroke-width="1.4"/></svg></span>
    <span><svg width="14" height="10" viewBox="0 0 14 10"><path d="M1 5h12M9 1l4 4-4 4" stroke="#333" fill="none" stroke-width="1.4"/></svg></span>
  </div>
</section>

<footer class="abs site-footer">
  <div class="abs brand footer-brand">
    <span class="brand-mark" style="width:96px;height:96px;background:var(--white)"></span>
    <span class="brand-name" style="color:var(--white)"><span style="font-size:56px">valtrix</span><br><span style="font-size:15px;font-family:'Red Hat Text',sans-serif">MECHANICAL DESIGN</span></span>
  </div>
  <nav class="abs footer-nav"><a href="#">Home</a><a href="#">About Us</a><a href="#">Our Services</a><a href="#">Portfolio</a><a href="#">Contact Us</a></nav>
  <div class="abs social"><span></span><span></span><span></span></div>
  <p class="abs copyright">Valtrix Mechanical Design 2025 &copy;</p>
</footer>
<a class="abs to-top"><svg width="12" height="8" viewBox="0 0 12 8"><path d="M1 7l5-5 5 5" stroke="#fff" fill="none" stroke-width="1.6"/></svg></a>

</body>
</html>
```